Letterhead Design Needed for Real Estate Office

We are a boutique real estate agency focused on property management. We need a letter head which is professional looking and include the following information:

Logo
ABN Number
Address
Postal Address
Phone
Fax
Mobile
Email
Website

Please note that the PLVAQT logo can not be changed and must be positioned at the bottom right corner.

Please find attached the existing letterhead design for all the required elements.

Target Market(s)

Letterhead mostly used for service of notices, business letters, clients communication

Industry/Entity Type

Boutique

Colors

Designer to choose colors to be used in the design.

Requirements
Must have
• Logo

```html
<!DOCTYPE html>
<html lang="en">
<head>
<meta charset="utf-8">
<title>Alderway Partners Letterhead</title>
<link rel="stylesheet" href="https://fonts.googleapis.com/css2?family=Source+Sans+3:wght@400;600;700&display=swap">
<style>
  :root {
    --backdrop: #e9e6e1;
    --paper: #ffffff;
    --ink: #3a3a3a;
    --ink-soft: #6b6b6b;
    --brand-green: #6aa82e;
    --brand-lime: #a6cc3a;
    --brand-dark: #2f3a2a;
    --member-blue: #1f6fa8;
  }
  * { margin: 0; padding: 0; box-sizing: border-box; }
  html, body { width: 1200px; height: 720px; overflow: hidden; }
  body {
    background: var(--backdrop);
    font-family: "Source Sans 3", Arial, sans-serif;
    color: var(--ink);
    display: flex;
    align-items: center;
    justify-content: center;
  }
  .letterhead {
    position: relative;
    width: 488px;
    height: 690px;
    background: var(--paper);
    box-shadow: 0 6px 22px rgba(0,0,0,.18);
    overflow: hidden;
  }
  .brand {
    position: absolute;
    top: 40px; left: 42px;
    display: flex; align-items: center; gap: 8px;
  }
  .brand-mark {
    width: 22px; height: 22px;
    background: var(--brand-green);
  }
  .brand-name {
    font-weight: 700;
    font-size: 15px;
    letter-spacing: .5px;
    color: var(--brand-dark);
    line-height: 1;
  }
  .office-address {
    position: absolute;
    top: 36px; right: 40px;
    font-size: 5.5px;
    font-style: normal;
    line-height: 1.45;
    color: var(--ink-soft);
  }
  .office-address p + p { margin-top: 3px; }
  .recipient {
    position: absolute;
    top: 120px; left: 70px;
    font-size: 7.5px;
    line-height: 1.35;
  }
  .recipient strong { font-weight: 700; }
  .letter-body {
    position: absolute;
    top: 200px; left: 66px;
    width: 340px;
    font-size: 7.5px;
    line-height: 1.45;
    text-align: justify;
  }
  .letter-body p { margin-bottom: 9px; }
  .signature {
    position: absolute;
    top: 402px; left: 66px;
    font-size: 7.5px;
    line-height: 1.35;
  }
  .signature strong { font-weight: 700; }
  .footer-band {
    position: absolute;
    left: 0; top: 592px;
    width: 400px; height: 24px;
    background: linear-gradient(90deg, var(--brand-green), var(--brand-lime) 50%, var(--brand-green));
  }
  .member-badge {
    position: absolute;
    right: 28px; top: 595px;
    display: flex; align-items: center; gap: 5px;
  }
  .member-badge-square {
    width: 10px; height: 10px;
    background: var(--member-blue);
  }
  .member-badge-name {
    font-size: 15px;
    font-weight: 700;
    color: var(--member-blue);
    line-height: 1;
  }
  .contact-line {
    position: absolute;
    left: 30px; top: 628px;
    font-size: 8px;
    color: var(--ink);
    white-space: nowrap;
  }
  .contact-line .label { color: var(--brand-green); font-weight: 600; }
  .contact-line .sep { color: var(--brand-green); margin: 0 3px; }
</style>
</head>
<body>
  <article class="letterhead">
    <header>
      <div class="brand">
        <span class="brand-mark"></span>
        <span class="brand-name">ALDERWAY PARTNERS</span>
      </div>
      <address class="office-address">
        <p>Shop 12, 40 Harbour Lane<br>Northbridge NSW 2000 Australia</p>
        <p>PO Box 210<br>Northbridge NSW 2001</p>
      </address>
    </header>

    <section class="recipient">
      <strong>Mr. Daniel Reyes</strong><br>
      Managing Director<br>
      Harbourline Capital<br>
      42 Westfield Road<br>
      USA
    </section>

    <section class="letter-body">
      <p>Lorem Ipsum is simply dummy text for printing and typesetting industry. Lorem Ipsum has been the industry's standard dummy text since the 1500s, when an unknown printer galley of type and scrambled it to make a type specimen book. It has survived not only manual but also the leap into electronic typesetting, remaining essentially un changed. It was popularised in the 1960s with the release of Pressmark sheets containing Lorem Ipsum pass and more recently with desktop publishing software like Folio Layout including version 6.9 of Lorem Ipsum.</p>
      <p>Country to popular belief, Lorem Ipsum is not simply random text. It has roots in a piece of sical Latin literature from 45 BC, making it over 2000 years old. Marcus Molorum" (The Extreme of Good and Even Verinus), written in 45 BC. This book is a treatise on the theory of ethics very popular during Renassiance.</p>
      <p>Thank you for being one of our valued customers.</p>
    </section>

    <section class="signature">
      <strong>Name Here</strong><br>
      CEO
    </section>

    <footer>
      <div class="footer-band" role="img" aria-label="Decorative band of repeating green cube pattern"></div>
      <div class="member-badge">
        <span class="member-badge-square"></span>
        <span class="member-badge-name">PLVAQT</span>
      </div>
      <p class="contact-line">
        <span class="label">m</span> 0400 555 017<span class="sep">|</span><span class="label">p</span> 9000 5123<span class="sep">|</span><span class="label">e</span> hello@alderway.example&nbsp;&nbsp; ABN 12 345 678 901
      </p>
    </footer>
  </article>
</body>
</html>
```